Startup online payment business - Sporting / Golf, Swift Tee payment

Background:
Our business name is "Swift Tee" we provide online payments for golfing services via our website. We currently have a logo used on our website. No other design style has been developed. Our aim is to remove cash payments for service at golf clubs.

Our Key Values:
Quick and easy
Formal and polite
Fun with professional boundary
Mate-ship relationships
100% online digital

What we want from you:
Marketing design to be used on posters and stickers in a retail setting to direct customers to our online payment Chanel.
Design must incorporate attached logo, URL swifttee.com.au and our key values can act as a guide the type of design. We have used color Hex#007672 for logo background. We are open to use other colors.

Target Market(s)

Golf clubs and golf players

Industry/Entity Type

Golf Course

Font styles to use
Sans Serif

Requirements
Must have
• Directions to online payment via URL: swifttee.com.au
Nice to have
• We like the idea of the slogan: No Cash - No worries. Have attached home screen that will be available from URL link. Consideration if using mobile phone in image. Push the online payment and steps 1. Visit swifttee.com 2. Select club 3. Confirm payment
Should not have
• Cartoons

```html
<!DOCTYPE html>
<html lang="en">
<head>
<meta charset="utf-8">
<title>Swift Tee – No Cash, No Worries</title>
<link rel="stylesheet" href="https://fonts.googleapis.com/css2?family=Bebas+Neue&family=Great+Vibes&family=Mukta:wght@400&display=swap">
<style>
  :root {
    --teal: #007672;
    --green: #2b8559;
    --forest: #2f6d50;
    --sage: #568e89;
    --white: #ffffff;
    --ink: #111111;
  }
  * { margin: 0; padding: 0; box-sizing: border-box; }
  html, body { width: 896px; height: 1200px; overflow: hidden; background: var(--teal); }
  .poster { position: relative; width: 896px; height: 1200px; overflow: hidden; background: var(--teal); }
  .backdrop { position: absolute; inset: 0; }
  .brand-name {
    position: absolute; left: 0; right: 0; top: 80px;
    text-align: center; color: var(--white);
    font-family: "Bebas Neue", sans-serif; font-size: 170px; line-height: 1;
    letter-spacing: 6px;
  }
  .slogan-band {
    position: absolute; left: 39px; top: 325px; width: 817px; height: 110px;
    background: var(--white);
    display: flex; align-items: center; justify-content: center;
    color: var(--teal); font-family: "Bebas Neue", sans-serif;
    font-size: 98px; line-height: 1; padding-top: 8px; letter-spacing: 1px;
  }
  .values-title { position: absolute; left: 0; right: 0; top: 448px; text-align: center; color: var(--white); }
  .values-title .script { display: block; font-family: "Great Vibes", cursive; font-size: 78px; line-height: 1; margin-left: 6px; }
  .values-title .heading { display: block; font-family: "Bebas Neue", sans-serif; font-size: 92px; line-height: 1; margin-top: -16px; }
  .value { position: absolute; width: 216px; height: 216px; }
  .value svg { position: absolute; inset: 0; }
  .value p {
    position: absolute; left: 18px; right: 18px; top: 68px; bottom: 16px;
    display: flex; align-items: center; justify-content: center; text-align: center;
    font-family: "Mukta", sans-serif; font-size: 27px; line-height: 1.18; color: var(--ink);
  }
  .v1 { left: 91px;  top: 609px; }
  .v2 { left: 340px; top: 609px; }
  .v3 { left: 588px; top: 609px; }
  .v4 { left: 212px; top: 817px; }
  .v5 { left: 460px; top: 817px; }
  .url-box {
    position: absolute; left: 122px; top: 1074px; width: 652px; height: 110px;
    background: var(--white); color: var(--teal);
    font-family: "Bebas Neue", sans-serif; font-size: 100px; line-height: 1;
    display: flex; align-items: flex-end; justify-content: center; padding-bottom: 4px; letter-spacing: 2px;
  }
  .url-label {
    position: absolute; left: 250px; top: 1052px; width: 397px; height: 45px;
    background: var(--teal); border: 1.5px solid var(--white); color: var(--white);
    font-family: "Bebas Neue", sans-serif; font-size: 40px; line-height: 1;
    display: flex; align-items: center; justify-content: center; padding-top: 4px; letter-spacing: 0.5px;
  }
</style>
</head>
<body>
<main class="poster">
  <svg class="backdrop" width="896" height="1200" viewBox="0 0 896 1200" aria-hidden="true">
    <rect width="896" height="1200" fill="var(--teal)"/>
    <path d="M0 0 H352 Q340 40 352 90 H0 Z" fill="var(--green)"/>
    <path d="M352 0 H650 L700 52 H352 Q340 30 352 0 Z" fill="var(--forest)"/>
    <rect x="0" y="0" width="54" height="150" fill="var(--green)"/>
    <rect x="0" y="228" width="54" height="470" fill="var(--sage)"/>
    <path d="M842 260 L896 300 V520 H842 Z" fill="var(--sage)"/>
    <path d="M842 740 Q896 760 896 790 V900 L842 960 Z" fill="var(--green)"/>
    <path d="M0 775 H54 V1200 H0 Z" fill="var(--green)"/>
    <path d="M842 1040 L896 990 V1200 H780 Z" fill="var(--sage)"/>
    <rect x="54" y="52" width="788" height="1097" fill="var(--teal)" stroke="var(--white)" stroke-width="1.5"/>
    <path d="M39 345 L54 330 V345 Z M856 345 L842 330 V345 Z M39 435 L54 450 V435 Z M856 435 L842 450 V435 Z" fill="var(--forest)"/>
  </svg>

  <h1 class="brand-name">Swift Tee</h1>

  <div class="slogan-band">NO CASH - NO WORRIES</div>

  <h2 class="values-title"><span class="script">Our</span><span class="heading">KEY VALUES:</span></h2>

  <svg width="0" height="0" aria-hidden="true" style="position:absolute">
    <defs>
      <symbol id="value-badge" viewBox="0 0 216 216">
        <circle cx="108" cy="108" r="107" fill="var(--white)" stroke="var(--green)" stroke-width="1.5"/>
        <path d="M29 34 A107 107 0 0 1 187 34 Q108 98 29 34 Z" fill="var(--green)"/>
        <path d="M92 23 H112 M92 23 V46 H115 V36" fill="none" stroke="#a9cdb7" stroke-width="2.5"/>
        <path d="M97 31 L104 41 L122 18" fill="none" stroke="var(--white)" stroke-width="4" stroke-linecap="round" stroke-linejoin="round"/>
      </symbol>
    </defs>
  </svg>

  <div class="value v1"><svg viewBox="0 0 216 216"><use href="#value-badge"/></svg><p>Quick and easy</p></div>
  <div class="value v2"><svg viewBox="0 0 216 216"><use href="#value-badge"/></svg><p>Formal and polite</p></div>
  <div class="value v3"><svg viewBox="0 0 216 216"><use href="#value-badge"/></svg><p>Fun with professional boundary</p></div>
  <div class="value v4"><svg viewBox="0 0 216 216"><use href="#value-badge"/></svg><p>Mate-ship relation-ships</p></div>
  <div class="value v5"><svg viewBox="0 0 216 216"><use href="#value-badge"/></svg><p>100% online digital</p></div>

  <div class="url-box">SWIFTTEE.COM.AU</div>
  <div class="url-label">ONLINE PAYMENT VIA URL:</div>
</main>
</body>
</html>
```